Business card for acupunctist in Melbourne. Specialises in Fertility, pre and post natal care, pain

I am looking for a business card which is going to catch people eyes. Two sided, one side in a muted colour (keeping it feminine) (pink or yellow???)maybe with a little simple logo or picture, the other side I was thinking white with 3 colours (pink grey and yellow... Had these in mind.
Info on the card
Maren Quillby Acupuncture

Dr Maren Quillby (TCM Acupuncture)
Acupuncture for balancing body and mind.
Verdant Osprey Clinic
14 Corran Lane, Eastwood 3071.
96274158
0438215074
Marentcm@quorvenmail.com

Some other little logo/ designs I have liked are as follows:
http://www.tessrolfeclinic.com/rates-and-insurance/
http://www.corabethwinslow.com/
http://www.zd-needlework.co.uk/

Target Market(s)

professional women, people in pain, active people, people seeking a healthy lifefstyle.

Industry/Entity Type

Business

Font styles to use
Serif
Sans Serif

Colors
eea4c8
fde08a
aaaaaa

Requirements
Must have
• Must be eye catching, but not too loud and busy. Subltle is good. Simple is also good. The logo could be something that represents growth and health and nurturing. Again not too elaborate, very simple.
Thankyou
Should not have
• Electric colours, crazy fonts, Pictures of yin and yang, candles, or bodies.

```html
<!DOCTYPE html>
<html lang="en">
<head>
<meta charset="utf-8">
<title>Maren Quillby Acupuncture – Business Card</title>
<link rel="stylesheet" href="https://fonts.googleapis.com/css2?family=Arimo:wght@400;700&display=swap">
<style>
  :root {
    --backdrop: #0d3c4e;
    --amber-deep: #f0a12a;
    --amber-light: #ffd94a;
    --ink: #2a2118;
    --card-white: #f8f8f8;
    --panel-grey: #ebebea;
    --rose: #e8338e;
    --leaf-green: #5cb83a;
    --text-dark: #222222;
  }
  html, body {
    margin: 0;
    width: 1200px;
    height: 1000px;
    overflow: hidden;
    background: var(--backdrop);
    font-family: "Arimo", Arial, sans-serif;
  }
  .canvas {
    position: relative;
    width: 1200px;
    height: 1000px;
  }
  .card {
    position: absolute;
    width: 560px;
    height: 340px;
    overflow: hidden;
    box-shadow: 0 10px 30px rgba(0,0,0,0.35);
  }
  .card-front {
    left: 90px;
    top: 110px;
    background: linear-gradient(135deg, var(--amber-deep) 0%, var(--amber-light) 100%);
  }
  .card-front .facets {
    position: absolute;
    inset: 0;
  }
  .brand {
    position: absolute;
    left: 0;
    right: 0;
    top: 70px;
    text-align: center;
  }
  .brand-dot {
    width: 56px;
    height: 56px;
    border-radius: 50%;
    background: var(--ink);
    margin: 0 auto 24px;
  }
  .brand-name {
    margin: 0;
    font-weight: 700;
    font-size: 34px;
    line-height: 1.15;
    color: var(--ink);
  }
  .card-back {
    left: 550px;
    top: 560px;
    background: var(--card-white);
  }
  .card-back .panel {
    position: absolute;
    inset: 0;
  }
  .practitioner {
    position: absolute;
    left: 30px;
    top: 72px;
  }
  .practitioner-name {
    margin: 0;
    font-weight: 700;
    font-size: 33px;
    color: var(--rose);
  }
  .practitioner-title {
    margin: 8px 0 0;
    font-weight: 700;
    font-size: 17px;
    color: var(--leaf-green);
  }
  .practice {
    position: absolute;
    left: 30px;
    bottom: 32px;
    font-weight: 700;
    font-size: 13px;
    color: var(--text-dark);
  }
  .practice p { margin: 0 0 16px; }
  .practice p:last-child { margin-bottom: 0; }
  .contact {
    position: absolute;
    right: 28px;
    top: 140px;
    text-align: right;
    font-weight: 700;
    font-size: 13px;
    color: var(--text-dark);
  }
  .contact p { margin: 0 0 16px; }
</style>
</head>
<body>
<main class="canvas">
  <section class="card card-front" aria-label="Card front">
    <svg class="facets" width="560" height="340" viewBox="0 0 560 340" aria-hidden="true">
      <polygon points="0,0 280,170 0,340" fill="rgba(0,0,0,0.04)"/>
      <polygon points="560,0 280,170 560,340" fill="rgba(255,255,255,0.08)"/>
      <polygon points="0,340 280,170 560,340" fill="rgba(255,255,255,0.05)"/>
    </svg>
    <div class="brand">
      <div class="brand-dot"></div>
      <h1 class="brand-name">Maren Quillby<br>Acupuncture</h1>
    </div>
  </section>

  <section class="card card-back" aria-label="Card back">
    <svg class="panel" width="560" height="340" viewBox="0 0 560 340" aria-hidden="true">
      <polygon points="0,330 300,95 560,95 560,340 0,340" fill="var(--panel-grey)"/>
    </svg>
    <div class="practitioner">
      <h2 class="practitioner-name">Dr Maren Quillby</h2>
      <p class="practitioner-title">(TCM Acupuncture)</p>
    </div>
    <div class="practice">
      <p>Acupuncture for balancing body and mind.</p>
      <p>Verdant Osprey Clinic</p>
      <p>14 Corran Lane, Eastwood 3071.</p>
    </div>
    <div class="contact">
      <p>96274158</p>
      <p>0438215074</p>
      <p>Marentcm@quorvenmail.com</p>
    </div>
  </section>
</main>
</body>
</html>
```